brightwave - Property Management DL Card

I am after a savvy designer to cut through junk mail! so many real estate agents use flyers to promote themselves and their business and usually sales. We are a property management firm (residential) and we want to represent landlords that have existing investment properties and need a quality agent to represent them. Can you help?
DL size, will be printed and delivered to mailboxes. For a look at our website go to www.brightwavehq.com.au. Keep it simple and clutter free.
it is to be double sided - with one side to be simple and clear - just our website, logo and telephone number on the back.
attached is our logo and our telephone number is 1300 42 18 96
the above are 2 essential elements to be included + our email address: admin@brightwavehq.com.au
also attached are our transparent price list

Target Market(s)
property investors,
people that manage properties themselves
Industry/Entity Type
Property Management
Other font styles liked:
- arial
Look and feel

```html
<!DOCTYPE html>
<html lang="en">
<head>
<meta charset="utf-8">
<title>brightwave property group – DL card</title>
<link rel="stylesheet" href="https://fonts.googleapis.com/css2?family=Arimo:wght@400;700&display=swap">
<style>
  :root{
    --ink:#111111;
    --charcoal:#1e1e1e;
    --paper:#ffffff;
    --red:#e3221c;
    --col-value:#cddcdf;
    --col-casual:#d6efe7;
    --col-basic:#b68b70;
    --col-plus:#cfd3d6;
    --col-ultimate:#e3b97b;
  }
  *{margin:0;padding:0;box-sizing:border-box}
  html,body{width:1173px;height:1200px;overflow:hidden;background:var(--paper)}
  body{position:relative;font-family:"Arimo",Arial,sans-serif;color:var(--ink)}

  /* ---------- Back side ---------- */
  .card-back{position:absolute;left:0;top:0;width:1173px;height:584px;overflow:hidden;background:var(--paper)}
  .phone-bar{position:absolute;left:0;top:0;width:760px;height:60px;
    background:linear-gradient(90deg,#111 0%,#2a2a2a 45%,rgba(40,40,40,0) 100%);
    color:var(--paper);font-size:38px;letter-spacing:2px;line-height:60px;padding-left:14px}
  .photo-city{position:absolute;left:-14px;top:107px;width:484px;height:484px;border-radius:50%;
    background:radial-gradient(circle at 45% 40%,#9a9a9a 0%,#5e5e5e 45%,#2f2f2f 80%,#1c1c1c 100%)}
  .photo-lounge{position:absolute;left:739px;top:-13px;width:456px;height:456px;border-radius:50%;
    background:radial-gradient(circle at 50% 45%,#f4f4f4 0%,#dcdcdc 55%,#bdbdbd 100%)}
  .back-name{position:absolute;left:470px;top:205px;width:540px;text-align:center;
    font-weight:400;color:var(--ink);line-height:1.1}
  .back-name .name{display:block;font-size:88px}
  .back-name .sub{display:block;font-size:46px;margin-top:6px}
  .web-bar{position:absolute;left:457px;top:524px;width:716px;height:56px;
    background:linear-gradient(90deg,rgba(40,40,40,0) 0%,#555 35%,#2a2a2a 100%);
    color:var(--paper);font-size:30px;line-height:56px;text-align:right;padding-right:16px}

  /* ---------- Front side ---------- */
  .card-front{position:absolute;left:0;top:618px;width:1173px;height:560px;overflow:hidden;background:var(--charcoal)}
  .photo-harbour{position:absolute;left:0;top:0;width:480px;height:560px;
    background:linear-gradient(180deg,#6d6d6d 0%,#8d8d8d 35%,#4a4a4a 65%,#9a9a9a 85%,#3a3a3a 100%)}
  .front-name-box{position:absolute;left:81px;top:13px;width:302px;height:289px;
    background:linear-gradient(180deg,rgba(20,20,20,.95),rgba(30,30,30,.8));
    display:flex;flex-direction:column;justify-content:center;align-items:center;
    color:var(--paper);font-weight:400;line-height:1.15}
  .front-name-box .name{font-size:44px}
  .front-name-box .sub{font-size:24px;margin-top:4px}
  .front-phone{position:absolute;left:34px;top:525px;color:var(--paper);font-size:35px;letter-spacing:2px;line-height:1}

  .contact-strip{position:absolute;left:477px;top:0;width:696px;height:60px;color:var(--paper);font-size:20px;
    display:flex;justify-content:space-between;align-items:center;padding:0 14px 0 4px}
  .price-head{position:absolute;left:477px;top:60px;width:696px;height:72px;background:var(--paper)}
  .price-head .art{position:absolute;right:0;top:0;width:470px;height:72px;
    background:linear-gradient(90deg,rgba(255,255,255,0) 0%,#c9d6d8 30%,#7a4a46 55%,#e6e6e6 65%,#3c5a8a 80%,#b33b35 100%)}
  .price-head .mini-name{position:absolute;left:10px;top:14px;line-height:1.1;color:var(--ink);font-weight:400}
  .mini-name .name{display:block;font-size:24px}
  .mini-name .sub{display:block;font-size:14px}
  .price-head .tag{position:absolute;left:240px;top:12px;background:var(--red);color:var(--paper);
    font-size:12px;line-height:18px;padding:3px 10px;white-space:nowrap}

  .fee-table{position:absolute;left:477px;top:132px;width:696px;border-collapse:collapse;table-layout:fixed;background:var(--paper);font-size:10px}
  .fee-table td,.fee-table th{height:15px;padding:0 4px;white-space:nowrap;overflow:hidden;text-align:center;font-weight:400}
  .fee-table .desc{text-align:left;font-weight:700}
  .fee-table .desc small{font-weight:400;font-size:6px}
  .fee-table .value{text-align:left;background:var(--col-value)}
  .fee-table .value b{display:inline-block;width:34px;text-align:right;margin-right:4px}
  .casual{background:var(--col-casual)}
  .basic{background:var(--col-basic)}
  .plus{background:var(--col-plus)}
  .ultimate{background:var(--col-ultimate)}
  .fee-table tr.dark td,.fee-table tr.dark th{background:var(--ink);color:var(--paper);font-size:10px}
  .fee-table tr.plans th{height:38px;line-height:1.2}
  .fee-table .rate{color:var(--red);font-size:14px;font-weight:700;display:block}
  .fee-table tr.section td{height:20px;font-weight:700}
  .fee-table tr.footer td{height:18px;font-size:10px}
  .fee-table tr.spacer td{height:5px}
</style>
</head>
<body>

<section class="card-back">
  <div class="photo-city" role="img" aria-label="Black and white aerial photo of a harbour city skyline and cable-stayed bridge"></div>
  <div class="photo-lounge" role="img" aria-label="Soft grey photo of a bright modern living room with lounge and coffee table"></div>
  <div class="phone-bar">1300 42 18 96</div>
  <div class="back-name">
    <span class="name">brightwave</span>
    <span class="sub">property group</span>
  </div>
  <div class="web-bar">www.brightwavehq.com.au</div>
</section>

<section class="card-front">
  <div class="photo-harbour" role="img" aria-label="Black and white photo of a harbour, bridge and waterfront city"></div>
  <div class="front-name-box">
    <span class="name">brightwave</span>
    <span class="sub">property group</span>
  </div>
  <div class="front-phone">1300 42 18 96</div>

  <div class="contact-strip">
    <span>Website: www.brightwavehq.com.au</span>
    <span>Email: admin@brightwavehq.com.au</span>
  </div>

  <div class="price-head">
    <div class="art" role="img" aria-label="Abstract colourful architectural photo banner"></div>
    <div class="mini-name"><span class="name">brightwave</span><span class="sub">property group</span></div>
    <div class="tag">brightwave PROPERTY MANAGEMENT<br>FEE STRUCTURE</div>
  </div>

  <table class="fee-table">
    <colgroup><col style="width:239px"><col style="width:124px"><col style="width:78px"><col style="width:78px"><col style="width:77px"><col style="width:100px"></colgroup>
    <tr class="dark plans"><th>DESCRIPTION</th><th></th><th>CASUAL</th><th>BASIC<span class="rate">4.0%</span></th><th>PLUS<span class="rate">5.0%</span></th><th>ULTIMATE<span class="rate">6.0%</span></th></tr>
    <tr class="dark"><td>LETTING FEES</td><td>ESTIMATED VALUE</td><td>EXPENSE</td><td>EXPENSE</td><td>EXPENSE</td><td>EXPENSE</td></tr>
    <tr><td class="desc">Letting fee</td><td class="value"></td><td class="casual">2 Weeks</td><td class="basic">1 Week</td><td class="plus">1 Week</td><td class="ultimate">1 Week</td></tr>
    <tr class="dark section"><td colspan="2">PROPERTY MANAGEMENT</td><td></td><td></td><td></td><td></td></tr>
    <tr class="spacer"><td></td><td class="value"></td><td class="casual"></td><td class="basic"></td><td class="plus"></td><td class="ultimate"></td></tr>
    <tr><td class="desc">Routine Inspections</td><td class="value"><b>$90</b>Per Inspection</td><td class="casual">N/A</td><td class="basic">1 Per Year</td><td class="plus">2 Per Year</td><td class="ultimate">3 Per Year</td></tr>
    <tr><td class="desc">Coordinate Repairs and Maintenance</td><td class="value"><b>$40</b>Per Hour</td><td class="casual">N/A</td><td class="basic">Included</td><td class="plus">Included</td><td class="ultimate">Included</td></tr>
    <tr><td class="desc">Transfer of Utilities</td><td class="value"><b>$40</b>Per Hour</td><td class="casual">N/A</td><td class="basic">Included</td><td class="plus">Included</td><td class="ultimate">Included</td></tr>
    <tr><td class="desc">Payment of Property Expenses</td><td class="value"><b>$40</b>Per Hour</td><td class="casual">N/A</td><td class="basic">Included</td><td class="plus">Included</td><td class="ultimate">Included</td></tr>
    <tr><td class="desc">Administration Fees</td><td class="value"><b>$5</b>Per Month</td><td class="casual">N/A</td><td class="basic">Included</td><td class="plus">Included</td><td class="ultimate">Included</td></tr>
    <tr><td class="desc">Postage &amp; Handling Fees</td><td class="value"><b>$5</b>Per Month</td><td class="casual">N/A</td><td class="basic">Included</td><td class="plus">Included</td><td class="ultimate">Included</td></tr>
    <tr><td class="desc">Monthly Landlord Statements</td><td class="value"><b>$5</b>Per Month</td><td class="casual">N/A</td><td class="basic">Included</td><td class="plus">Included</td><td class="ultimate">Included</td></tr>
    <tr><td class="desc">Annual Market Update and Rent Review</td><td class="value"><b>$80</b>Per Year</td><td class="casual">N/A</td><td class="basic">Included</td><td class="plus">Included</td><td class="ultimate">Included</td></tr>
    <tr><td class="desc">End of Year Financial Statements</td><td class="value"><b>$25</b>Per Year</td><td class="casual">N/A</td><td class="basic"></td><td class="plus">Included</td><td class="ultimate">Included</td></tr>
    <tr><td class="desc">Lease Preparation Fee</td><td class="value"><b>$25</b>Per Year</td><td class="casual">N/A</td><td class="basic"></td><td class="plus">Included</td><td class="ultimate">Included</td></tr>
    <tr><td class="desc">Tribunal Preparation</td><td class="value"><b>$60</b>Per Hour</td><td class="casual">N/A</td><td class="basic"></td><td class="plus"></td><td class="ultimate">Included</td></tr>
    <tr><td class="desc">Tribunal Attendance</td><td class="value"><b>$60</b>Per Hour</td><td class="casual">N/A</td><td class="basic"></td><td class="plus"></td><td class="ultimate">Included</td></tr>
    <tr class="spacer"><td></td><td class="value"></td><td class="casual"></td><td class="basic"></td><td class="plus"></td><td class="ultimate"></td></tr>
    <tr class="dark section"><td colspan="2">MARKETING</td><td></td><td></td><td></td><td></td></tr>
    <tr class="spacer"><td></td><td class="value"></td><td class="casual"></td><td class="basic"></td><td class="plus"></td><td class="ultimate"></td></tr>
    <tr><td class="desc">Advertising Copy</td><td class="value"><b>$90</b></td><td class="casual">N/A</td><td class="basic">Included</td><td class="plus">Included</td><td class="ultimate">Included</td></tr>
    <tr><td class="desc">Social Media <small>(social feeds, video, networks)</small></td><td class="value"><b>$90</b></td><td class="casual">N/A</td><td class="basic">Included</td><td class="plus">Included</td><td class="ultimate">Included</td></tr>
    <tr><td class="desc">Internet Marketing <small>(homefinder / rentspot / brightwavehq)</small></td><td class="value"><b>$190</b></td><td class="casual">N/A</td><td class="basic"></td><td class="plus">Included</td><td class="ultimate">Included</td></tr>
    <tr><td class="desc">Professional Photography</td><td class="value"><b>$125</b></td><td class="casual">N/A</td><td class="basic"></td><td class="plus"></td><td class="ultimate">Included</td></tr>
    <tr><td class="desc">Signboard</td><td class="value"><b>$150</b></td><td class="casual">N/A</td><td class="basic"></td><td class="plus"></td><td class="ultimate">Included</td></tr>
    <tr><td class="desc">Floor Plan</td><td class="value"><b>$125</b></td><td class="casual">N/A</td><td class="basic"></td><td class="plus"></td><td class="ultimate">Included</td></tr>
    <tr class="spacer"><td></td><td class="value"></td><td class="casual"></td><td class="basic"></td><td class="plus"></td><td class="ultimate"></td></tr>
    <tr class="dark footer"><td colspan="6">brightwave are the property management specialists</td></tr>
  </table>
</section>

</body>
</html>
```